Boutique Fitness Facility needs a new meal plan design that is as hot as our workouts!

We are about to host our 6 week Coral Tide program and we need to have a great looking meal plan handout created that we can give to all of our participants.

I have attached an example of our current full meal plan, for a reference only.

As in the example I've provided, I'd like to have certain areas color coded such as the proteins being Blue, Fats -yellow, Carbs - orange and veggies- green.

These colors will corollate to the Breakfast - snack - lunch - snack - Dinner graph that I've provided and would like to have added to the new handout.

I would like our logo placed at the top and beneath the logo have the text "Coral Tide Challenge"

The flyer should be of a summer influence in colors and design and
All text should be easy to read.

Thank you and I look forward to seeing your design!

```html
<!DOCTYPE html>
<html lang="en">
<head>
<meta charset="utf-8">
<title>Coral Tide Challenge – Meal Plan</title>
<link href="https://fonts.googleapis.com/css2?family=Anton&family=Oswald:wght@500;600&family=Poppins:wght@400;500;600;700;800&display=swap" rel="stylesheet">
<style>
:root{
  --ink:#141414;
  --panel:#e6e6e8;
  --band:#e9e9eb;
  --blue:#3a4bb3;
  --yellow:#f7cf0c;
  --orange:#f28a1e;
  --green:#4fb24a;
  --white:#ffffff;
  --grey:#a8a8a8;
  --text-dark:#333;
  --stage:#e9eaec;
}
*{box-sizing:border-box;margin:0;padding:0}
html,body{width:1200px;height:2410px;overflow:hidden;background:var(--stage);font-family:"Poppins",sans-serif}
.sheet{position:absolute;left:0;top:437px;width:1200px;height:1535px;overflow:hidden;color:var(--white)}
.sheet-backdrop{position:absolute;inset:0;background:radial-gradient(ellipse at 50% 55%,#3a3530 0%,#1e1c1a 45%,#111 100%)}
.brand{position:absolute;top:58px;left:0;width:100%;text-align:center;font-family:"Poppins",sans-serif;font-weight:800;font-size:104px;line-height:1;color:var(--white);letter-spacing:-2px}
.tagline{position:absolute;top:168px;left:0;width:100%;text-align:center;font-weight:700;font-size:16px;letter-spacing:5px;color:var(--yellow)}
.title{position:absolute;top:196px;left:0;width:100%;text-align:center;font-family:"Anton",sans-serif;font-weight:400;font-size:64px;letter-spacing:4px;color:var(--yellow)}

.food-card{position:absolute;top:300px;width:240px;background:var(--panel);border-radius:22px;padding:62px 14px 16px 16px;color:var(--text-dark)}
.food-tab{position:absolute;top:-16px;left:-12px;height:54px;width:218px;border-radius:14px 0 40px 0;transform:skewX(-10deg);font-weight:700;font-size:27px;letter-spacing:1px;display:flex;align-items:center;padding-left:24px}
.food-tab span{transform:skewX(10deg)}
.card-protein{left:80px;height:453px}
.card-fats{left:345px;height:369px}
.card-carbs{left:618px;height:369px}
.card-veg{left:889px;height:369px}
.card-protein .food-tab{background:var(--blue);color:var(--yellow)}
.card-fats .food-tab{background:var(--yellow);color:var(--ink)}
.card-carbs .food-tab{background:var(--orange);color:var(--ink)}
.card-veg .food-tab{background:var(--green);color:var(--white)}
.food-list{list-style:none}
.food-list li{display:flex;gap:12px;font-size:16px;line-height:1.15;margin-bottom:11px}
.food-list li::before{content:"";flex:0 0 18px;height:18px;border-radius:50%;margin-top:1px;background:var(--dot)}
.card-protein{--dot:var(--blue)}
.card-fats{--dot:var(--yellow)}
.card-carbs{--dot:var(--orange)}
.card-veg{--dot:var(--green)}
.card-carbs .food-list li{margin-bottom:10px}
.card-veg .food-list li{margin-bottom:13px}

.note-bar{position:absolute;top:693px;left:356px;width:778px;height:43px;display:flex;font-size:19px;font-weight:500;border:2px solid var(--yellow)}
.note-label{background:var(--ink);color:var(--yellow);font-weight:700;font-size:24px;width:100px;display:flex;align-items:center;justify-content:center}
.note-light{background:var(--green);flex:0 0 330px;display:flex;align-items:center;padding-left:12px}
.note-heavy{background:var(--orange);color:var(--ink);flex:1;display:flex;align-items:center;padding-left:20px}

.meal-band{position:absolute;top:769px;left:62px;width:1072px;height:221px;background:var(--band)}
.meal-band svg{display:block}

.fuel-banner{position:absolute;top:1016px;left:62px;width:420px;height:82px;background:var(--yellow);clip-path:polygon(0 0,100% 0,93% 100%,0 100%);color:var(--ink);font-family:"Anton",sans-serif;font-size:34px;display:flex;align-items:center;padding-left:24px;letter-spacing:.5px}
.fuel-intro{position:absolute;top:1028px;left:494px;width:650px;font-size:17px;line-height:1.2;font-weight:500}

.tip{position:absolute;text-align:center;width:320px}
.tip-head{display:flex;align-items:center;height:80px;position:relative;margin:0 auto 6px;width:300px}
.tip-badge{width:80px;height:80px;border-radius:50%;background:var(--yellow);border:6px solid var(--ink);box-shadow:0 0 0 3px var(--yellow);position:relative;z-index:2;flex:none}
.tip-badge::after{content:"";position:absolute;inset:18px;border-radius:50%;border:5px solid var(--ink)}
.tip-pill{background:var(--band);color:var(--ink);font-weight:700;font-size:22px;line-height:1.05;text-align:left;height:64px;border-radius:0 32px 32px 0;margin-left:-30px;padding-left:42px;padding-right:16px;flex:1;display:flex;align-items:center;white-space:nowrap}
.tip p{font-size:16px;line-height:1.2}
.tip-1{left:65px;top:1112px}
.tip-2{left:440px;top:1112px}
.tip-3{left:815px;top:1112px}
.tip-4{left:235px;top:1285px}
.tip-5{left:672px;top:1285px}
.divider{position:absolute;border-left:2px dashed #bbb;width:0}
</style>
</head>
<body>
<main class="sheet">
  <div class="sheet-backdrop" role="img" aria-label="Dim gym interior photograph with an athlete training under low light"></div>

  <header>
    <div class="brand">PulseForge</div>
    <div class="tagline">PERSONAL GROUP TRAINING</div>
    <h1 class="title">CORAL TIDE CHALLENGE</h1>
  </header>

  <section class="food-card card-protein">
    <div class="food-tab"><span>PROTEIN</span></div>
    <ul class="food-list">
      <li>4-6 oz Chicken Breast</li>
      <li>4-6oz Turkey Breast</li>
      <li>4-6 oz Filet Mignon</li>
      <li>4-6 oz Flank Steak</li>
      <li>4-6 oz Salmon</li>
      <li>4-6 oz Tuna</li>
      <li>4-6 oz Cod</li>
      <li>4-6 oz Cottage Cheese</li>
      <li>4-6 oz Greek Yogurt</li>
      <li>4-6 oz Tofu</li>
      <li>3-5 egg whites + 1 whole egg</li>
    </ul>
  </section>

  <section class="food-card card-fats">
    <div class="food-tab"><span>FATS</span></div>
    <ul class="food-list">
      <li>¼ - ½ Avocado</li>
      <li>1 tbs Olive Oil</li>
      <li>1 small handful Almonds, Walnuts, Cashews</li>
    </ul>
  </section>

  <section class="food-card card-carbs">
    <div class="food-tab"><span>CARBS</span></div>
    <ul class="food-list">
      <li>3 – 4oz Sweet Potato</li>
      <li>¼ - ½ cup White Rice</li>
      <li>¼ - ½ cup Quinoa</li>
      <li>¼ - ½ cup Oatmeal</li>
      <li>¾ cup Blueberries</li>
      <li>¾ cup Strawberries</li>
      <li>¾ cup Raspberries</li>
      <li>1 med. Apple</li>
      <li>1 small orange</li>
      <li>1 small grapefruit</li>
    </ul>
  </section>

  <section class="food-card card-veg">
    <div class="food-tab"><span>VEGETABLES</span></div>
    <ul class="food-list">
      <li>1 Scoop Powdered Greens</li>
      <li>1 Cup Sautéed Spinach</li>
      <li>1 Cup Sautéed Kale, Broccoli</li>
      <li>1 Cup Sautéed Bell Pepper</li>
      <li>1 Cup Sautéed Carrots</li>
      <li>1 Cup Sautéed Zucchini</li>
    </ul>
  </section>

  <div class="note-bar">
    <div class="note-label">NOTE</div>
    <div class="note-light">&lt; 150 lbs stick to smaller portions</div>
    <div class="note-heavy">&gt; 150 lbs stick to larger portions.</div>
  </div>

  <section class="meal-band">
    <svg width="1072" height="221" viewBox="0 0 1072 221" font-family="Oswald, sans-serif">
      <defs>
        <marker id="arrowhead" viewBox="0 0 10 10" refX="6" refY="5" markerWidth="3" markerHeight="3" orient="auto">
          <path d="M0 0 L10 5 L0 10 z" fill="#3a4bb3"/>
        </marker>
        <g id="ring-base">
          <path d="M100 20 A80 80 0 0 1 169.3 140" fill="none" stroke="#3a4bb3" stroke-width="34"/>
          <path d="M169.3 140 A80 80 0 0 1 30.7 140" fill="none" stroke="#4fb24a" stroke-width="34"/>
        </g>
      </defs>

      <g transform="translate(12,10)">
        <use href="#ring-base"/>
        <path d="M30.7 140 A80 80 0 0 1 100 20" fill="none" stroke="#f28a1e" stroke-width="34"/>
        <circle cx="100" cy="100" r="62" fill="#a8a8a8" stroke="#fff" stroke-width="4"/>
        <text x="100" y="109" text-anchor="middle" font-size="24" font-weight="500" fill="#222">BREAKFAST</text>
        <text x="32" y="64" font-size="14" fill="#222">1</text>
        <text x="165" y="84" font-size="14" fill="#fff">1</text>
        <text x="96" y="196" font-size="14" fill="#222">1</text>
      </g>

      <g transform="translate(220,0)" fill="none" stroke="#3a4bb3" stroke-width="10" stroke-linecap="round">
        <path d="M12 80 Q40 45 72 72" marker-end="url(#arrowhead)"/>
        <path d="M102 80 Q130 45 162 72" marker-end="url(#arrowhead)"/>
      </g>
      <g transform="translate(240,100)">
        <polygon points="0,22 12,0 108,0 120,22" fill="#4fb24a"/>
        <text x="60" y="17" text-anchor="middle" font-size="14" font-weight="600" fill="#111" font-family="Poppins, sans-serif">SNACK</text>
        <text x="60" y="50" text-anchor="middle" font-size="16" fill="#222" font-family="Poppins, sans-serif">1/2 PORTION</text>
        <text x="60" y="70" text-anchor="middle" font-size="16" fill="#222" font-family="Poppins, sans-serif">OF PROTEIN</text>
      </g>

      <g transform="translate(406,10)">
        <use href="#ring-base"/>
        <path d="M30.7 140 A80 80 0 0 1 100 20" fill="none" stroke="#f28a1e" stroke-width="34"/>
        <circle cx="100" cy="100" r="62" fill="#a8a8a8" stroke="#fff" stroke-width="4"/>
        <text x="100" y="111" text-anchor="middle" font-size="28" font-weight="500" fill="#222">LUNCH</text>
        <text x="32" y="64" font-size="14" fill="#222">1</text>
        <text x="165" y="84" font-size="14" fill="#fff">1</text>
        <text x="96" y="196" font-size="14" fill="#222">1</text>
      </g>

      <g transform="translate(608,0)" fill="none" stroke="#3a4bb3" stroke-width="10" stroke-linecap="round">
        <path d="M12 80 Q40 45 72 72" marker-end="url(#arrowhead)"/>
        <path d="M102 80 Q130 45 162 72" marker-end="url(#arrowhead)"/>
      </g>
      <g transform="translate(628,100)">
        <polygon points="0,22 12,0 108,0 120,22" fill="#4fb24a"/>
        <text x="60" y="17" text-anchor="middle" font-size="14" font-weight="600" fill="#111" font-family="Poppins, sans-serif">SNACK</text>
        <text x="60" y="50" text-anchor="middle" font-size="16" fill="#222" font-family="Poppins, sans-serif">1/2 PORTION</text>
        <text x="60" y="70" text-anchor="middle" font-size="16" fill="#222" font-family="Poppins, sans-serif">OF PROTEIN</text>
      </g>

      <g transform="translate(804,10)">
        <use href="#ring-base"/>
        <path d="M30.7 140 A80 80 0 0 1 100 20" fill="none" stroke="#f7cf0c" stroke-width="34"/>
        <circle cx="100" cy="100" r="62" fill="#a8a8a8" stroke="#fff" stroke-width="4"/>
        <text x="100" y="111" text-anchor="middle" font-size="28" font-weight="500" fill="#222">DINNER</text>
        <text x="32" y="64" font-size="14" fill="#222">1</text>
        <text x="165" y="84" font-size="14" fill="#fff">1</text>
        <text x="96" y="196" font-size="14" fill="#222">1</text>
      </g>
    </svg>
  </section>

  <div class="fuel-banner">FUEL YOUR CORAL TIDE!</div>
  <p class="fuel-intro">This plan isn't about starving yourself – it's about sculpting a lean, toned physique by shredding fat while preserving muscle.<br>Here's how to maximize your results</p>

  <article class="tip tip-1">
    <div class="tip-head"><span class="tip-badge"></span><span class="tip-pill">Eat Like a<br>Champion</span></div>
    <p>Stick to this list as close as possible for maximum results, 7 Days A Week.</p>
  </article>
  <div class="divider" style="left:409px;top:1122px;height:110px"></div>
  <article class="tip tip-2">
    <div class="tip-head"><span class="tip-badge"></span><span class="tip-pill">Burn More Than<br>You Consume</span></div>
    <p>This is the golden rule! You need to burn more calories than you consume to create a deficit and force your body to tap into fat stores for energy.</p>
  </article>
  <div class="divider" style="left:805px;top:1122px;height:110px"></div>
  <article class="tip tip-3">
    <div class="tip-head"><span class="tip-badge"></span><span class="tip-pill">Prioritize<br>Protein</span></div>
    <p>Protein helps build and maintain muscle mass, which is crucial for boosting metabolism and burning more calories at rest.</p>
  </article>

  <article class="tip tip-4">
    <div class="tip-head"><span class="tip-badge"></span><span class="tip-pill">Maximize<br>Sleep</span></div>
    <p>When sleep-deprived, your body produces more ghrelin (hunger hormone) and less leptin (satiety hormone). Aim for 7-8 hours of quality sleep nightly.</p>
  </article>
  <div class="divider" style="left:600px;top:1300px;height:130px"></div>
  <article class="tip tip-5">
    <div class="tip-head"><span class="tip-badge"></span><span class="tip-pill">Consistency is<br>King/Queen</span></div>
    <p>Don't expect overnight results. Stick to your plan, track your progress, and celebrate small victories. Remember, slow and steady wins the shred race!</p>
  </article>
</main>
</body>
</html>
```